New Hotel Showcase Website

We plan to launch a website called www.fernlodgings.net which showcases the world’s best new hotels. We want a mock up for 2 pages: the homepage (page 1) and the individual hotel page (page 2). We are looking for a design which combines simplicity while highlighting images/features of the hotel. Because the theme of the site is new hotels it is important that the design somehow emphasizes the age of each hotel listed – both on the homepage and then on the individual hotel page.

NOTE: WE WANT A CREATIVE, NEW APPROACH TO DISPLAYING HOTELS. NOT JUST A COPY OF CURRENT HOTEL WEBSITES.

The design should consider unique and creative ways of helping users to navigate the homepage (page 1) based on the age, location or style of the hotel they are interested in. The individual hotel page(page 2) can be more standard by clearly setting out hotel photos, feature lists, reviews, contact details and potential discounts. There is no booking system needed as this is not a hotel booking website.

The design should ideally be compatible with a content management system such as Page Forge. In terms of reference materials we like sites similar to:

http://www.quillwanderer.net
http://www.bobandkayporter.net
http://www.craftinns.net
http://www.pebblestays.net

These sites are designed far more simply than large booking sites such as www.voyaro.net, www.roomsy.net or even jaunt ledger. However, we are not looking for a copy of the above. We are looking for a design that presents hotels in a novel way and would be seen by the industry as a unique way of displaying new hotels.
Updates

Dear Designers - we have received quite a few entries already. Thank you. However, none of the designs submitted have responded to our brief. They are all copies or derivatives of current hotel websites which is not what we are looking for. We want (a) a new and creative approach to a hotel website and (b) one which creatively uses the age of the hotel (ie. 1 month old, 6 months old etc).

It will require creative thinking and new ideas. We wanted to challenge designers to come up with something new. Thanks.

```html
<!DOCTYPE html>
<html lang="en">
<head>
<meta charset="utf-8">
<title>Fern Lodgings – Hotel Card</title>
<link href="https://fonts.googleapis.com/css2?family=Montserrat:wght@400;500;600;700;800&family=Inter:wght@400;500&display=swap" rel="stylesheet">
<style>
  :root{
    --page-bg:#e6e6e6;
    --chrome:#1c1c1d;
    --accent-blue:#4d86e0;
    --ink:#161616;
    --white:#ffffff;
    --muted:#b9b9b9;
    --star:#f5a800;
    --badge-red:#d9262c;
    --rule:#bdbdbd;
  }
  *{box-sizing:border-box;margin:0;padding:0}
  html,body{width:900px;height:1200px;overflow:hidden;background:var(--page-bg)}
  body{position:relative;font-family:"Montserrat",sans-serif}

  .screen{position:absolute;left:120px;top:20px;width:660px;height:1160px;background:var(--chrome);overflow:hidden}

  .status-bar{position:absolute;left:0;top:0;width:100%;height:56px;color:var(--white);font-family:"Inter",sans-serif;font-size:23px}
  .status-bar .carrier{position:absolute;left:18px;top:14px;display:flex;align-items:center;gap:6px}
  .status-bar .clock{position:absolute;left:0;right:0;top:14px;text-align:center}
  .status-bar .power{position:absolute;right:18px;top:14px;display:flex;align-items:center;gap:8px}

  .site-header{position:absolute;left:0;top:56px;width:100%;height:120px}
  .menu-icon{position:absolute;left:36px;top:49px}
  .search-icon{position:absolute;right:36px;top:44px}
  .brand{position:absolute;left:0;right:0;top:34px;display:flex;align-items:center;justify-content:center;gap:12px;color:var(--white)}
  .brand-mark{width:14px;height:14px;border-radius:50%;background:var(--accent-blue)}
  .brand-name{font-size:30px;font-weight:500;letter-spacing:1px;line-height:36px}
  .header-note{position:absolute;left:0;right:0;top:78px;text-align:center;font-size:14px;font-weight:500;letter-spacing:1.2px;color:var(--muted)}

  .hotel-card{position:absolute;left:8px;top:176px;width:644px;height:972px;background:var(--white);border-top:5px solid var(--accent-blue);border-bottom:5px solid var(--accent-blue);overflow:hidden}

  .hotel-photo{position:absolute;left:0;top:0;width:100%;height:830px;
    background:linear-gradient(180deg,#c9d3cc 0%,#e2dcc4 18%,#8fa7b0 20%,#6b8a9c 30%,#a89a84 35%,#d8d2c4 38%,#3fc6dc 42%,#2cb6d2 62%,#8c8676 68%,#6f6a60 76%,#d6d4d0 88%,#ffffff 100%)}
  .slide-arrow{position:absolute;top:370px}
  .slide-arrow.prev{left:14px}
  .slide-arrow.next{right:14px}

  .hotel-name{position:absolute;left:32px;top:660px;font-size:72px;font-weight:800;line-height:78px;color:var(--ink);letter-spacing:-1px}

  .rating{position:absolute;left:30px;top:848px;display:flex;gap:14px}
  .price{position:absolute;left:462px;top:836px;width:190px;padding:0 0 6px 0;border-bottom:2px solid var(--ink);font-size:28px;font-weight:400;color:var(--ink)}
  .price strong{font-weight:700}

  .hotel-meta{position:absolute;left:0;top:890px;width:100%;height:70px;display:flex;align-items:center}
  .location{margin-left:34px;font-size:24px;letter-spacing:3px;color:var(--ink);font-weight:400}
  .location strong{font-weight:700}
  .meta-divider{width:2px;height:36px;background:var(--rule)}
  .meta-divider.first{margin-left:28px}
  .style-icon{margin:0 26px}
  .age-badge{margin-left:28px;background:var(--badge-red);color:var(--white);font-size:15px;font-weight:600;padding:2px 7px;line-height:20px}
</style>
</head>
<body>
  <main class="screen">
    <div class="status-bar">
      <div class="carrier">
        <svg width="72" height="14" viewBox="0 0 72 14"><circle cx="7" cy="7" r="6" fill="#fff"/><circle cx="21" cy="7" r="6" fill="#fff"/><circle cx="35" cy="7" r="6" fill="#fff"/><circle cx="49" cy="7" r="5.2" fill="none" stroke="#fff" stroke-width="1.4"/><circle cx="63" cy="7" r="5.2" fill="none" stroke="#fff" stroke-width="1.4"/></svg>
        <span>KESTREL</span>
        <svg width="24" height="18" viewBox="0 0 24 18"><path d="M2 6a14 14 0 0 1 20 0M5.5 9.5a9 9 0 0 1 13 0M9 13a4 4 0 0 1 6 0" fill="none" stroke="#fff" stroke-width="2.2" stroke-linecap="round"/><circle cx="12" cy="16" r="1.6" fill="#fff"/></svg>
      </div>
      <div class="clock">4:21 PM</div>
      <div class="power">
        <svg width="14" height="24" viewBox="0 0 14 24"><path d="M2 7l10 10-5 5V2l5 5L2 17" fill="none" stroke="#bbb" stroke-width="1.8"/></svg>
        <span>22%</span>
        <svg width="50" height="22" viewBox="0 0 50 22"><rect x="1" y="1" width="44" height="20" rx="3" fill="none" stroke="#fff" stroke-width="2"/><rect x="4" y="4" width="9" height="14" fill="#fff"/><rect x="46" y="7" width="3" height="8" fill="#fff"/></svg>
      </div>
    </div>

    <header class="site-header">
      <svg class="menu-icon" width="32" height="24" viewBox="0 0 32 24"><path d="M1 2h30M1 9h30M1 16h30M1 23h22" stroke="#fff" stroke-width="2"/></svg>
      <div class="brand">
        <span class="brand-mark"></span>
        <span class="brand-name">Fernlodgings</span>
      </div>
      <div class="header-note">FRESHLY OPENED STAYS</div>
      <svg class="search-icon" width="34" height="34" viewBox="0 0 34 34"><circle cx="13" cy="13" r="10" fill="none" stroke="#fff" stroke-width="3"/><path d="M20.5 20.5L31 31" stroke="#fff" stroke-width="3.4" stroke-linecap="round"/></svg>
    </header>

    <article class="hotel-card">
      <div class="hotel-photo" role="img" aria-label="Photo of an infinity pool with thatched parasols and sun loungers overlooking the sea"></div>
      <svg class="slide-arrow prev" width="40" height="70" viewBox="0 0 40 70"><path d="M34 4L6 35l28 31" fill="none" stroke="#fff" stroke-width="4" stroke-linecap="round" stroke-linejoin="round" opacity=".85"/></svg>
      <svg class="slide-arrow next" width="40" height="70" viewBox="0 0 40 70"><path d="M6 4l28 31L6 66" fill="none" stroke="#fff" stroke-width="4" stroke-linecap="round" stroke-linejoin="round" opacity=".85"/></svg>

      <h1 class="hotel-name">AZURE<br>KELYON</h1>

      <div class="rating" aria-label="5 stars">
        <svg width="108" height="20" viewBox="0 0 108 20" fill="var(--star)">
          <path id="star" d="M9 1l2.4 5.4 5.9.6-4.4 4 1.3 5.8L9 13.8 3.8 16.8l1.3-5.8L.7 7l5.9-.6z"/>
          <use href="#star" x="30"/><use href="#star" x="60"/><use href="#star" x="90"/>
        </svg>
        <svg width="20" height="20" viewBox="0 0 20 20" fill="var(--star)"><path d="M9 1l2.4 5.4 5.9.6-4.4 4 1.3 5.8L9 13.8 3.8 16.8l1.3-5.8L.7 7l5.9-.6z"/></svg>
      </div>
      <div class="price"><strong>$92</strong>/Night</div>

      <div class="hotel-meta">
        <div class="location">MYKONOS, <strong>GREECE</strong></div>
        <span class="meta-divider first"></span>
        <svg class="style-icon" width="24" height="20" viewBox="0 0 24 20"><path d="M5 1h14l4 6-11 12L1 7z" fill="var(--ink)"/><path d="M1 7h22M8 1l4 18 4-18" stroke="#fff" stroke-width="1.2" fill="none"/></svg>
        <span class="meta-divider"></span>
        <span class="age-badge">3 months</span>
      </div>
    </article>
  </main>
</body>
</html>
```